Brochure for a paper wholesaler who wants to educate his print industry clients

We will be making a stapled informative brochure, that contains basic information about our paper products - the types of paper there is, their characteristics and other useful information.
As we are part of a paper wholesaler group in Europe - VORENT, we received a brochure in German that has this kind of information. The text in it is not as important. What is important is the layout of the document and how the text will appear in it (added in the uploaded files - 210915_Wiessenswertes_TBLK_F51.pdf).
We are allowed to tinker with this file and adjust it to our needs. So there are also .idml and .indd files available (also in the uploaded files).
We would like to keep the custom page size of 210 x290mm (8.3x11.4 in), or you can go up to 210x297mm (8.3x11.7 in).
What we want is a modern looking design that contains our companies red bordo and white/ grey colours to replace the existing green colours in this borchure. The pictures and appearance of the file can be changed according to your views and what you think would look good. We don't necessarily want to keep the same design, we just want the layout of the document be the same, as we will be placing our translated text into it. The VORENT logo should be replaced with our own logo (KUMET Logo.png).
As for how it could look, it could go together with our paper presentation, for which the design can be seen in the "KUMET Base - v2.pptx".
Holiday season, so have a lot of tasks to take care of and not as much time to check ArtHarbor as often.

```html
<!DOCTYPE html>
<html lang="en">
<head>
<meta charset="UTF-8">
<title>Presentation Guide – KUMET</title>
<link href="https://fonts.googleapis.com/css2?family=Josefin+Sans:wght@400;700&display=swap" rel="stylesheet">
<style>
  :root {
    --backdrop: #e7e8ea;
    --paper: #ffffff;
    --ink: #232323;
    --ink-soft: #3b3b3b;
    --bordo: #6d2e31;
  }
  * { margin: 0; padding: 0; box-sizing: border-box; }
  html, body {
    width: 1200px;
    height: 1200px;
    overflow: hidden;
    background: var(--backdrop);
    font-family: "Josefin Sans", sans-serif;
  }
  .page {
    position: absolute;
    left: 200px;
    top: 40px;
    width: 801px;
    height: 1120px;
    background: var(--paper);
    box-shadow: 0 4px 18px rgba(0, 0, 0, 0.08);
  }
  .page-title {
    position: absolute;
    top: 138px;
    left: 0;
    width: 100%;
    text-align: center;
    font-size: 57px;
    font-weight: 700;
    color: var(--ink);
    letter-spacing: 1.5px;
    padding-left: 8px;
  }
  .contents {
    position: absolute;
    left: 120px;
    top: 436px;
    width: 559px;
    list-style: none;
  }
  .contents-item {
    display: flex;
    justify-content: space-between;
    align-items: flex-end;
    height: 62.4px;
    padding: 0 2px 5px 2px;
    border-bottom: 2.7px solid var(--ink-soft);
    font-size: 25px;
    font-weight: 700;
    color: var(--ink-soft);
    letter-spacing: 1.3px;
  }
  .contents-item:first-child { height: 37px; }
  .footer-band {
    position: absolute;
    left: 0;
    top: 1020px;
    width: 100%;
    height: 52px;
    background: var(--bordo);
  }
  .brand-plate {
    position: absolute;
    left: 23.5px;
    top: 0;
    width: 208px;
    height: 52px;
    background: var(--paper);
    display: flex;
    align-items: center;
    gap: 18px;
    padding-left: 25px;
  }
  .brand-square {
    width: 30px;
    height: 30px;
    border: 1.5px solid var(--bordo);
  }
  .brand-name {
    font-size: 15px;
    font-weight: 400;
    color: var(--bordo);
    letter-spacing: 14px;
  }
</style>
</head>
<body>
  <main class="page">
    <h1 class="page-title">Presentation Guide</h1>

    <ol class="contents">
      <li class="contents-item"><span>ABOUT KUMET</span><span>03</span></li>
      <li class="contents-item"><span>KUMET LOGISTICS</span><span>04</span></li>
      <li class="contents-item"><span>KUMET AND VORENT</span><span>05</span></li>
      <li class="contents-item"><span>PERFORMANCE</span><span>06</span></li>
      <li class="contents-item"><span>WHAT WE OFFER</span><span>08</span></li>
      <li class="contents-item"><span>OUR SUPPLIERS</span><span>13</span></li>
      <li class="contents-item"><span>OUR PRODUCTS</span><span>14</span></li>
    </ol>

    <footer class="footer-band">
      <div class="brand-plate">
        <span class="brand-square"></span>
        <span class="brand-name">KUMET</span>
      </div>
    </footer>
  </main>
</body>
</html>
```